Business card for denture clinic Plendora

We need a new business card with our new logo. We are a denture clinic in New Zealand with our target market being 45+ years old. We would need a space on the back to write our patients next appointment on. We would space for only one appointment rather than a list. We will attach a photo showing an example of this. But of course, we would like to see your twist on this. We want it to be bold and easy to read and a good mixture of professional but modern. We have attached our logo to be used on the card.

Target Market(s)

People aged 45+ needing dentures

Industry/Entity Type

Dental

Contact Information for Business Card

We want our logo on the front and the space to write an appointment on the back. I've attached an example our our old business card showing this. We need to have the technicians details on the front.

Font styles to use
Sans Serif

Colors
0255a3
919191
fbfbfb

Requirements
Must have
• The following details:
• Ray Dunmore BDT, PGDipCDentTech Kerrow
• Dental Prosthetist
• Phone numbers: 0800 47 3215
• 09 517 2943
• Email: ray@plendora.co.nz
• www.plendora.co.nz
• Address: 148 Mirelle Road
• Norvale South
• Brenmouth 0745
Nice to have
• We would like our business cards to have more than just two colours as we want them to be more vibrant. We have uploaded an example of a business card we liked that showed this.

```html
<!DOCTYPE html>
<html lang="en">
<head>
<meta charset="utf-8">
<title>Plendora – Business Card</title>
<link rel="stylesheet" href="https://fonts.googleapis.com/css2?family=Source+Sans+3:ital,wght@0,400;0,600;0,700;1,400&display=swap">
<style>
  :root {
    --brand-blue: #0271bd;
    --accent-orange: #e4612b;
    --text-grey: #4a4a4a;
    --tag-grey: #8d8d8d;
    --card-white: #ffffff;
    --field-fill: #f4f4f4;
    --backdrop: #eeeeee;
    --rule: #cfcfcf;
  }
  * { box-sizing: border-box; margin: 0; padding: 0; }
  html, body {
    width: 1200px; height: 987px; overflow: hidden;
    background: var(--backdrop);
    font-family: "Source Sans 3", sans-serif;
  }
  .card {
    position: absolute; left: 293px;
    width: 615px; height: 350px;
    border-radius: 19px;
    box-shadow: 0 2px 6px rgba(0,0,0,0.12);
  }
  .card--front { top: 130px; background: var(--card-white); }
  .card--back { top: 505px; background: var(--brand-blue); color: var(--card-white); }

  .brand { position: absolute; text-align: center; width: 300px; }
  .brand__square { display: block; margin: 0 auto; width: 54px; height: 54px; }
  .brand__name {
    display: block; font-weight: 600; font-size: 33px; letter-spacing: 1.5px;
    line-height: 1; text-transform: uppercase;
  }
  .brand__tagline {
    display: block; font-size: 12.5px; letter-spacing: 2.4px; text-transform: uppercase;
  }
  .card--front .brand { left: 20px; top: 129px; }
  .card--front .brand__square { background: var(--brand-blue); }
  .card--front .brand__name { color: var(--brand-blue); margin-top: 10px; }
  .card--front .brand__tagline { color: var(--tag-grey); margin-top: 3px; }

  .divider {
    position: absolute; left: 312px; top: 57px; width: 1px; height: 228px;
    background: var(--rule);
  }
  .details { position: absolute; left: 336px; top: 52px; color: var(--text-grey); }
  .details__name { color: var(--brand-blue); font-weight: 700; font-size: 22px; line-height: 26px; }
  .details__name small { font-size: 16px; }
  .details__quals { color: var(--brand-blue); font-weight: 700; font-size: 17px; line-height: 22px; }
  .details__role { color: var(--accent-orange); font-size: 16.5px; line-height: 22px; }
  .details__address { margin-top: 9px; font-size: 16.5px; line-height: 23px; }
  .contacts { list-style: none; margin-top: 9px; }
  .contacts li { display: flex; align-items: center; font-size: 16px; line-height: 24px; }
  .contacts svg { width: 16px; height: 16px; margin-right: 9px; fill: var(--brand-blue); flex: none; }

  .card--back .brand { left: 157px; top: 52px; }
  .card--back .brand__square { width: 56px; height: 56px; background: var(--card-white); }
  .card--back .brand__name { color: var(--card-white); font-size: 34px; margin-top: 12px; }
  .card--back .brand__tagline { color: #dbe9f5; margin-top: 2px; }

  .appointment__title {
    position: absolute; left: 0; right: 0; top: 198px; text-align: center;
    font-weight: 600; font-size: 23px;
  }
  .field {
    position: absolute; top: 274px; width: 240px; height: 43px; border-radius: 22px;
    background: var(--field-fill); color: var(--brand-blue);
    font-style: italic; font-size: 18px; line-height: 43px; padding-left: 17px;
  }
  .field--date { left: 30px; }
  .field--time { left: 346px; }
</style>
</head>
<body>
  <section class="card card--front">
    <div class="brand">
      <span class="brand__square"></span>
      <span class="brand__name">Plendora</span>
      <span class="brand__tagline">Smile Care Clinic</span>
    </div>
    <div class="divider"></div>
    <div class="details">
      <p class="details__name">RAY DUNMORE <small>BDT,</small></p>
      <p class="details__quals">PGDipCDentTech Kerrow</p>
      <p class="details__role">Dental Prosthetist</p>
      <p class="details__address">148 Mirelle Road<br>Norvale South, Brenmouth 0745</p>
      <ul class="contacts">
        <li><svg viewBox="0 0 16 16" aria-hidden="true"><path d="M3.5 1.5l2.5 0 1.2 3.2-1.6 1.2c.8 1.8 2.2 3.2 4 4l1.2-1.6 3.2 1.2v2.5c0 .9-.7 1.5-1.6 1.4C6.6 13 3 9.4 2.6 3.1 2.5 2.2 2.6 1.5 3.5 1.5z"/></svg>0800 47 3215</li>
        <li><svg viewBox="0 0 16 16" aria-hidden="true"><path d="M4.5 1h7c.6 0 1 .4 1 1v12c0 .6-.4 1-1 1h-7c-.6 0-1-.4-1-1V2c0-.6.4-1 1-1zm.7 2v9h5.6V3zM8 12.6a.8.8 0 100 1.6.8.8 0 000-1.6z"/></svg>09 517 2943</li>
        <li><svg viewBox="0 0 16 16" aria-hidden="true"><path d="M1.5 3.5h13v9h-13zM2.6 4.5 8 8.8l5.4-4.3zM2.5 5.6v5.9h11V5.6L8 10z"/></svg>ray@plendora.co.nz</li>
        <li><svg viewBox="0 0 16 16" aria-hidden="true"><path d="M8 1a7 7 0 100 14A7 7 0 008 1zm-1 2.2c-.6.8-1.6 1.1-1.5 2.2.1.9 1.4.8 1.7 1.7.3.9-.6 1.6-.2 2.6.4.9 1.2 1.6 1 2.7-.1.6-.3 1-.6 1.3A5.6 5.6 0 012.5 7c.7-1.9 2.4-3.4 4.5-3.8zm3.3.6a5.6 5.6 0 012.4 6.4c-.6-.5-1.4-.4-1.9-1.1-.5-.8.2-1.7-.4-2.4-.6-.7-1.6-.3-2-1.1-.3-.7.5-1.2 1.9-1.8z"/></svg>www.plendora.co.nz</li>
      </ul>
    </div>
  </section>

  <section class="card card--back">
    <div class="brand">
      <span class="brand__square"></span>
      <span class="brand__name">Plendora</span>
      <span class="brand__tagline">Smile Care Clinic</span>
    </div>
    <h2 class="appointment__title">Next Appointment</h2>
    <div class="field field--date">date:</div>
    <div class="field field--time">time:</div>
  </section>
</body>
</html>
```